bramblecrest paving card makeover

were a excavation/paving contractor from Monterey ca, I'm looking to have a card designed front and back that has company details on the front and a list of the services we offer on the back.

Target Market(s)

home owners property management companies

Industry/Entity Type

Contractor

Contact Information for Business Card

bramblecrest paving 418 larkmoor st Monterey ca. licensed, insured and bonded
lic#657920 gerald pinsky operations manager

Font styles to use
Serif
Sans Serif

Colors
f78f20

Requirements
Must have
• a list of my services on back, asphalt construction and maintenance, drainage, foundations, retaining walls, chip seals, excavation, grading, landscape ground work, interlocking paver, hydro-seeding, structured and driveway demolition, utility trenching and stump removal.
Nice to have
• my new domain and page address I'm acquiring from pixel bazaar.

```html
<!DOCTYPE html>
<html lang="en">
<head>
<meta charset="utf-8">
<title>Bramblecrest Paving – Business Card</title>
<link href="https://fonts.googleapis.com/css2?family=Oswald:wght@500&family=Work+Sans:ital,wght@0,400;1,400&family=Roboto:wght@400&display=swap" rel="stylesheet">
<style>
  :root {
    --backdrop: #141414;
    --card-top: #262626;
    --card-bottom: #1a1a1a;
    --orange: #f78f20;
    --white: #ffffff;
    --text-light: #e9e9e9;
  }
  html, body {
    margin: 0;
    padding: 0;
    width: 1200px;
    height: 897px;
    overflow: hidden;
    background: var(--backdrop);
  }
  .canvas {
    position: relative;
    width: 1200px;
    height: 897px;
  }
  .card {
    position: absolute;
    left: 303px;
    width: 595px;
    height: 339px;
    border-radius: 22px;
    overflow: hidden;
    background: linear-gradient(160deg, var(--card-top), var(--card-bottom));
    font-family: "Work Sans", sans-serif;
    color: var(--text-light);
  }
  .card--front { top: 92px; }
  .card--back { top: 469px; }

  .holder-name {
    position: absolute;
    left: 30px;
    top: 28px;
    margin: 0;
    font-family: "Oswald", sans-serif;
    font-weight: 500;
    font-size: 27px;
    letter-spacing: 0.3px;
    color: var(--orange);
    text-transform: uppercase;
    line-height: 1;
  }
  .holder-role {
    position: absolute;
    left: 30px;
    top: 61px;
    margin: 0;
    font-size: 14px;
    letter-spacing: 0.4px;
  }
  .address {
    position: absolute;
    left: 30px;
    top: 180px;
    margin: 0;
    font-size: 13.5px;
    line-height: 17px;
    letter-spacing: 0.3px;
    font-style: normal;
  }
  .contact-list {
    position: absolute;
    left: 30px;
    top: 229px;
    margin: 0;
    padding: 0;
    list-style: none;
    font-size: 14px;
    letter-spacing: 0.3px;
  }
  .contact-list li {
    display: flex;
    align-items: center;
    height: 19px;
  }
  .contact-list svg {
    width: 12px;
    height: 12px;
    margin-right: 10px;
    fill: var(--orange);
  }
  .accent { color: var(--orange); }

  .licence-band {
    position: absolute;
    left: 0;
    top: 299px;
    width: 100%;
    height: 27px;
    background: var(--orange);
    color: var(--white);
    font-style: italic;
    font-size: 14px;
    line-height: 27px;
    padding-left: 33px;
    box-sizing: border-box;
    letter-spacing: 0.3px;
  }

  .brand-mark {
    position: absolute;
    display: flex;
    flex-direction: column;
    align-items: center;
    gap: 10px;
    text-align: center;
    font-family: "Oswald", sans-serif;
    font-weight: 500;
    color: var(--white);
    text-transform: uppercase;
    line-height: 1.05;
  }
  .brand-mark__dot {
    border: 3px solid var(--white);
    border-radius: 50%;
  }
  .card--front .brand-mark {
    left: 318px;
    top: 88px;
    width: 210px;
    font-size: 34px;
  }
  .card--front .brand-mark__dot { width: 22px; height: 22px; }
  .card--back .brand-mark {
    left: 205px;
    top: 52px;
    width: 180px;
    font-size: 24px;
    gap: 8px;
  }
  .card--back .brand-mark__dot { width: 16px; height: 16px; }

  .services {
    position: absolute;
    left: 0;
    top: 226px;
    width: 100%;
    height: 113px;
    background: var(--orange);
    color: var(--white);
    font-family: "Roboto", sans-serif;
    text-align: center;
  }
  .services__title {
    margin: 8px 0 2px;
    font-size: 18.5px;
    font-weight: 400;
    line-height: 22px;
  }
  .services__list {
    margin: 0 auto;
    width: 540px;
    font-size: 14px;
    line-height: 19.2px;
  }
</style>
</head>
<body>
<main class="canvas">

  <section class="card card--front" aria-label="Card front">
    <h1 class="holder-name">Dorian Vell</h1>
    <p class="holder-role">Managing Director</p>

    <address class="address">418 Larkmoor St, Monterey,<br>California, CA</address>

    <ul class="contact-list">
      <li>
        <svg viewBox="0 0 24 24" aria-hidden="true"><path d="M6.6 10.8a15.1 15.1 0 0 0 6.6 6.6l2.2-2.2a1 1 0 0 1 1-.25 11.4 11.4 0 0 0 3.6.57 1 1 0 0 1 1 1V20a1 1 0 0 1-1 1A17 17 0 0 1 3 4a1 1 0 0 1 1-1h3.5a1 1 0 0 1 1 1c0 1.25.2 2.45.57 3.57a1 1 0 0 1-.25 1z"/></svg>
        +1 831 555 0147
      </li>
      <li>
        <svg viewBox="0 0 24 24" aria-hidden="true"><path d="M2 5h20v2l-10 6L2 7z M2 9l10 6 10-6v10H2z"/></svg>
        info@bramblecrestpaving.com
      </li>
      <li>
        <svg viewBox="0 0 24 24" aria-hidden="true"><path d="M12 2a10 10 0 1 0 0 20 10 10 0 0 0 0-20zm0 2c.9 0 2.2 1.9 2.8 5H9.2C9.8 5.9 11.1 4 12 4zM4.3 11h2.8a17 17 0 0 0 0 2H4.3a8 8 0 0 1 0-2zm4.8 0h5.8a15 15 0 0 1 0 2H9.1a15 15 0 0 1 0-2zm7.8 0h2.8a8 8 0 0 1 0 2h-2.8a17 17 0 0 0 0-2zM9.2 15h5.6c-.6 3.1-1.9 5-2.8 5s-2.2-1.9-2.8-5z"/></svg>
        www.<span class="accent">bramblecrestpaving</span>.com
      </li>
    </ul>

    <div class="brand-mark">
      <span class="brand-mark__dot" aria-hidden="true"></span>
      <span>Bramblecrest Paving</span>
    </div>

    <div class="licence-band">Lic# 657920</div>
  </section>

  <section class="card card--back" aria-label="Card back">
    <div class="brand-mark">
      <span class="brand-mark__dot" aria-hidden="true"></span>
      <span>Bramblecrest Paving</span>
    </div>

    <div class="services">
      <h2 class="services__title">SERVICES</h2>
      <p class="services__list">asphalt construction and maintenance | drainage | foundations | retaining walls, chip seals | excavation | grading | landscape ground work | interlocking paver, hydro-seeding | structured and driveway demolition, utility trenching and stump removal.</p>
    </div>
  </section>

</main>
</body>
</html>
```